Cylinder Packaging Design - Massage Balls Sports company

Package design needed for 1 x massage and 1 x double massage balls. please see images attached of the 2 products, both items will be stored in 1 x cardboard cylinder tube, samples also attached please ignore the designs as its the style of packaging that you are referring to.

Size of cylinder, length 21cm width 7.5cm

Final design should communicate health and fitness / physiotherapy / rehabilitation but also relating to our retail sports company, logo colour ect. please refer to our website www.kq3active.com for your reference and also to give you an idea who we are and what we do.

Attached are our 2 logos 1 x black and 1 x grey back grounds for you to work with.

```html
<!DOCTYPE html>
<html lang="en">
<head>
<meta charset="utf-8">
<title>KQ3 Active – Massage Ball Tube Packaging</title>
<link href="https://fonts.googleapis.com/css2?family=Russo+One&display=swap" rel="stylesheet">
<style>
  :root {
    --page-bg: #ffffff;
    --tube-dark: #0c1216;
    --tube-mid: #142027;
    --brand-blue: #1fa9cf;
    --brand-blue-bright: #3fd3f5;
    --beam-grey: #8a8f93;
    --brand-text: #ffffff;
    --lid-line: #000000;
  }
  html, body {
    margin: 0;
    padding: 0;
    width: 1200px;
    height: 1000px;
    overflow: hidden;
    background: var(--page-bg);
  }
  .packaging-canvas {
    display: block;
    width: 1200px;
    height: 1000px;
  }
  .brand-name {
    font-family: "Russo One", sans-serif;
    font-weight: 400;
    fill: var(--brand-text);
    text-anchor: middle;
  }
  .icon-frame {
    fill: none;
    stroke: var(--brand-blue);
    stroke-width: 3;
  }
  .icon-tile {
    fill: var(--brand-blue);
    opacity: 0.85;
  }
  .lid-line {
    stroke: var(--lid-line);
    stroke-width: 2;
  }
  .beam { fill: var(--beam-grey); opacity: 0.55; }
  .blue-stripe { fill: var(--brand-blue); }
</style>
</head>
<body>
<svg class="packaging-canvas" viewBox="0 0 1200 1000" xmlns="http://www.w3.org/2000/svg">
  <defs>
    <linearGradient id="tall-body" x1="305" y1="0" x2="565" y2="0" gradientUnits="userSpaceOnUse">
      <stop offset="0" stop-color="var(--tube-dark)"/>
      <stop offset="0.55" stop-color="var(--tube-mid)"/>
      <stop offset="0.68" stop-color="var(--brand-blue)"/>
      <stop offset="0.74" stop-color="var(--brand-blue-bright)"/>
      <stop offset="0.82" stop-color="var(--tube-mid)"/>
      <stop offset="1" stop-color="var(--tube-dark)"/>
    </linearGradient>
    <linearGradient id="short-body" x1="622" y1="0" x2="893" y2="0" gradientUnits="userSpaceOnUse">
      <stop offset="0" stop-color="var(--tube-dark)"/>
      <stop offset="0.62" stop-color="var(--tube-mid)"/>
      <stop offset="0.74" stop-color="var(--brand-blue)"/>
      <stop offset="0.8" stop-color="var(--brand-blue-bright)"/>
      <stop offset="0.88" stop-color="var(--tube-mid)"/>
      <stop offset="1" stop-color="var(--tube-dark)"/>
    </linearGradient>
    <clipPath id="tall-clip"><rect x="305" y="55" width="260" height="885"/></clipPath>
    <clipPath id="short-clip"><rect x="622" y="518" width="271" height="417"/></clipPath>
  </defs>

  <!-- Tall tube wrap -->
  <g class="tube tube-tall">
    <g clip-path="url(#tall-clip)">
      <rect x="305" y="55" width="260" height="885" fill="url(#tall-body)"/>
      <polygon class="blue-stripe" points="312,55 324,55 408,400 400,400"/>
      <polygon class="beam" points="305,140 305,200 430,430 440,420"/>
      <polygon class="beam" points="305,230 305,300 425,440"/>
      <polygon class="beam" points="432,560 372,940 340,940"/>
      <polygon class="beam" points="440,560 565,840 565,760"/>
      <polygon class="beam" points="436,560 520,940 490,940"/>
      <rect class="blue-stripe" x="428" y="560" width="5" height="380"/>
      <line class="lid-line" x1="305" y1="130" x2="565" y2="130"/>
    </g>
    <text class="brand-name" x="440" y="462" font-size="58">KQ3</text>
    <text class="brand-name" x="440" y="502" font-size="24">ACTIVE</text>
    <g class="icon-column">
      <rect class="icon-frame" x="405" y="758" width="56" height="172"/>
      <line class="icon-frame" x1="405" y1="815" x2="461" y2="815"/>
      <line class="icon-frame" x1="405" y1="872" x2="461" y2="872"/>
      <rect class="icon-tile" x="412" y="765" width="42" height="43" role="img" aria-label="Weightlifter icon"/>
      <rect class="icon-tile" x="412" y="822" width="42" height="43" role="img" aria-label="Footprints icon"/>
      <rect class="icon-tile" x="412" y="879" width="42" height="44" role="img" aria-label="Kettlebell icon"/>
    </g>
  </g>

  <!-- Short tube wrap -->
  <g class="tube tube-short">
    <g clip-path="url(#short-clip)">
      <rect x="622" y="518" width="271" height="417" fill="url(#short-body)"/>
      <polygon class="blue-stripe" points="622,598 622,606 735,665 738,660"/>
      <polygon class="beam" points="622,625 622,660 735,690"/>
      <polygon class="beam" points="748,730 690,935 665,935"/>
      <polygon class="beam" points="755,730 893,880 893,830"/>
      <polygon class="beam" points="752,730 820,935 795,935"/>
      <rect class="blue-stripe" x="756" y="730" width="4" height="205"/>
      <line class="lid-line" x1="622" y1="590" x2="893" y2="590"/>
    </g>
    <text class="brand-name" x="755" y="690" font-size="44">KQ3</text>
    <text class="brand-name" x="755" y="723" font-size="20">ACTIVE</text>
    <g class="icon-column">
      <rect class="icon-frame" x="733" y="785" width="50" height="148"/>
      <line class="icon-frame" x1="733" y1="834" x2="783" y2="834"/>
      <line class="icon-frame" x1="733" y1="883" x2="783" y2="883"/>
      <rect class="icon-tile" x="739" y="791" width="38" height="37" role="img" aria-label="Weightlifter icon"/>
      <rect class="icon-tile" x="739" y="840" width="38" height="37" role="img" aria-label="Footprints icon"/>
      <rect class="icon-tile" x="739" y="889" width="38" height="38" role="img" aria-label="Kettlebell icon"/>
    </g>
  </g>
</svg>
</body>
</html>
```